Harbor Bean Corp Business Card Design

Harbor Bean Corp is a local owner and operator of several coffee shops in Irving, TX. Google "Brew Bright Corner" for an example of one of our shops.We would like an image that is professional, but with a slight nod to the protestant religious nature of our backers.The name "Harbor Bean" is a play on the concept of "rivers of living water". It also conveys the concept of a "brewed with care". We desire to combine these concepts in the logo visualization, with the emphasis on the commercial side of the concept.

Target Market(s)

Upper class retail. No drive-through. Comfy lounges.

Industry/Entity Type

Coffee Shop

Contact Information for Business Card

Dale Mercer
Chief Operating Officer
Harbor Bean Corp
(832) 555 0147
dale@harborbean.example (address not yet active)

Requirements
Must have
• We do not have a logo yet. Need that as a part of the design.
• This needs to be original artwork. I need to own the art when the design is finished. I will look at submissions with stock artwork, but be advised that I will not accept the submission until original work is presented.

```html
<!DOCTYPE html>
<html lang="en">
<head>
<meta charset="utf-8">
<title>Harbor Bean Corp – Business Card</title>
<link rel="stylesheet" href="https://fonts.googleapis.com/css2?family=Oswald:wght@600&family=Open+Sans:wght@400&display=swap">
<style>
  :root {
    --canvas-bg: #e4e4e6;
    --card-top: #ffffff;
    --card-bottom: #efeff1;
    --coffee-brown: #6b2f17;
    --ink: #2b2b2b;
    --rule-grey: #c9c9cd;
    --muted-grey: #55555a;
  }
  * { margin: 0; padding: 0; box-sizing: border-box; }
  html, body {
    width: 1200px; height: 1200px; overflow: hidden;
    background: var(--canvas-bg);
  }
  .canvas {
    width: 1200px; height: 1200px;
    display: flex; flex-direction: column; align-items: center; justify-content: center;
    gap: 52px;
  }
  .card {
    position: relative;
    width: 900px; height: 514px;
    background: linear-gradient(160deg, var(--card-top) 0%, var(--card-bottom) 100%);
    box-shadow: 0 6px 18px rgba(0,0,0,0.18);
    overflow: hidden;
  }
  .card--front { border-bottom: 10px solid var(--coffee-brown); }

  .brand-name {
    font-family: "Oswald", sans-serif; font-weight: 600;
    color: var(--coffee-brown);
    text-transform: uppercase; letter-spacing: 1px;
    line-height: 1;
  }

  .card--front .brand-name {
    position: absolute; left: 90px; top: 118px;
    font-size: 54px;
  }
  .divider {
    position: absolute; left: 90px; top: 232px;
    width: 440px; height: 2px; background: var(--rule-grey);
  }
  .contact {
    position: absolute; left: 300px; top: 262px;
    font-style: normal;
    font-family: "Open Sans", sans-serif; font-weight: 400;
    color: var(--ink); font-size: 25px; line-height: 1.32;
  }
  .contact__name {
    font-family: "Oswald", sans-serif; font-weight: 600;
    color: var(--coffee-brown); text-transform: uppercase;
    font-size: 27px; letter-spacing: 0.5px; margin-bottom: 4px;
  }

  .card--back {
    display: flex; flex-direction: column; align-items: center; justify-content: center;
    gap: 26px;
  }
  .card--back .brand-name { font-size: 66px; }
  .tagline {
    font-family: "Open Sans", sans-serif; font-weight: 400;
    color: var(--muted-grey); font-size: 24px; letter-spacing: 16px;
    margin-left: 16px;
  }
</style>
</head>
<body>
  <main class="canvas">
    <section class="card card--front" aria-label="Business card, contact side">
      <div class="brand-name">Harbor Bean</div>
      <div class="divider"></div>
      <address class="contact">
        <div class="contact__name">Dale Mercer</div>
        <div>Chief Operating Officer</div>
        <div>Harbor Bean Corp</div>
        <div>(832) 555 0147</div>
        <div>dale@harborbean.example</div>
      </address>
    </section>

    <section class="card card--back" aria-label="Business card, brand side">
      <div class="brand-name">Harbor Bean</div>
      <p class="tagline">brewed with care</p>
    </section>
  </main>
</body>
</html>
```